A start up ecommerce site. Selling one item at the moment and hope to expand. Selling acrylic makeup organizers. It is a product for women. It stores all cosmetic/makeup.... a storage solution.
Its a womens product so it should be geared towards it. I have a logo that I will upload.
My shop: http://www.craftvendo.example/shop/GlossNestBoxes
Not the best photos, so if you know how to touch up it would be a plus.
Updates

I don't sell makeup.

competitors sites

http://www.vanityprism.example/#info

http://www.lucentbeautybox.example/

http://maribelpetal.example/

http://vanityprismholder.example/

 

Target Market(s)

Women

Industry/Entity Type

Shop

Requirements
Must have
• Social Media Logos. Twitter,Facebook,Google+ and Pinterest Like Buttons
Paywindle/Quorra
Shopping Cart
Main page with the product and description. Buy Now or add to cart button. Our policy, contact us, email register.
Nice to have
• Fun, Modern, Girly. Not over complicated and easy to navigate, simple.
Should not have
• Anything from the competitor.

```html
<!DOCTYPE html>
<html lang="en">
<head>
<meta charset="utf-8">
<title>GlossNest – Acrylic Makeup Organizer</title>
<link href="https://fonts.googleapis.com/css2?family=Arimo:wght@400;700&family=Source+Sans+3:wght@400;600&display=swap" rel="stylesheet">
<style>
:root{
  --black:#000;
  --pink:#f0124e;
  --grey-text:#9a9a9a;
  --body-text:#8a8a8a;
  --rule:#d4d4d4;
  --white:#fff;
  --page:#ececec;
}
*{margin:0;padding:0;box-sizing:border-box}
html,body{width:1200px;height:1009px;overflow:hidden}
body{position:relative;font-family:"Source Sans 3",sans-serif;
  background:radial-gradient(ellipse at 50% 30%,#fff 0%,#f3f3f3 45%,#e2e2e2 100%);color:var(--body-text)}
.abs{position:absolute}
.topbar{left:0;top:0;width:1200px;height:28px;background:var(--black);color:var(--white);
  font-family:Arimo,sans-serif;font-size:10.5px}
.topbar .links{position:absolute;left:201px;top:8px;word-spacing:2px}
.topbar .account{position:absolute;right:200px;top:8px;font-size:9.5px}
.logo{font-family:Arimo,sans-serif;font-weight:400;color:var(--black);letter-spacing:-0.5px}
.header-logo{left:205px;top:60px;font-size:36px}
.cart{left:700px;top:50px;display:flex;align-items:center;gap:8px;color:var(--pink);
  font-weight:600;font-size:12px}
.social{top:50px;display:flex;gap:6px;left:902px}
.social span{width:20px;height:20px;border:1px solid #c8c8c8;background:#f3f3f3;border-radius:2px;display:block}
.search{left:697px;top:94px;width:303px;height:28px;border:1px solid #cfcfcf;background:#f1f1f1;
  font-size:10px;color:#aaa;padding:7px 10px}
.search svg{position:absolute;right:8px;top:6px}
.search .sep{position:absolute;right:33px;top:5px;height:16px;border-left:1px solid #ddd}
.nav{left:199px;top:142px;width:802px;height:48px;background:var(--black);
  box-shadow:0 8px 6px -4px rgba(0,0,0,.35);display:flex;align-items:center;padding-left:23px}
.nav a{color:var(--pink);font-size:12px;text-decoration:none;padding:0 21px;border-right:1px dashed #666;line-height:18px}
.nav a:first-child{padding-left:0}
.nav a:last-child{border:none}
.banner{left:199px;top:213px;width:802px;height:305px;background:var(--black);
  box-shadow:0 6px 6px -3px rgba(0,0,0,.35)}
.photo-organizer{left:93px;top:27px;width:220px;height:210px;
  background:radial-gradient(ellipse,#6d6d70 0%,#2e2e30 55%,#0a0a0a 100%)}
.photo-cosmetics{left:401px;top:27px;width:264px;height:168px;
  background:radial-gradient(ellipse,#7a5a55 0%,#3a2a2a 55%,#050505 100%)}
.banner h1{position:absolute;left:337px;top:203px;color:var(--white);font-weight:600;font-size:33px;letter-spacing:-0.3px}
.banner p{position:absolute;left:336px;top:250px;color:var(--white);font-size:16px}
.banner svg{position:absolute;top:108px}
.product-photo{left:199px;top:558px;width:280px;height:278px;border:3px solid #c8c8c8;
  background:linear-gradient(160deg,#3d3d3d,#161616 60%,#2a2a2a)}
.intro{left:505px;top:560px;width:494px;font-size:10.5px;line-height:16px;color:var(--grey-text)}
.rule{height:1px;background:var(--rule);left:504px;width:498px}
.features{left:517px;top:666px;list-style:none;font-size:10.5px;line-height:17px;color:#8f8f8f}
.features li{position:relative;padding-left:10px}
.features li::before{content:"";position:absolute;left:0;top:7px;width:4px;height:4px;border-radius:50%;background:var(--pink)}
.features .sm{font-size:8.5px;line-height:14px}
.buy{left:515px;top:802px;width:139px;height:35px;border-radius:4px;border:1px solid #000;
  background:linear-gradient(#5a5a5a,#1b1b1b 50%,#000);color:#c9c9c9;font-family:Arimo,sans-serif;
  font-size:18px;text-align:center;line-height:33px}
.price{left:671px;top:802px;color:var(--pink);font-family:Arimo,sans-serif;font-size:35px}
.learn{left:766px;top:816px;color:var(--pink);font-family:Arimo,sans-serif;font-size:18px;text-decoration:underline}
.footer{left:0;top:850px;width:1200px;height:159px;background:var(--black)}
.news-title{left:201px;top:862px;color:var(--pink);font-family:Arimo,sans-serif;font-size:25px}
.email{left:198px;top:894px;width:282px;height:28px;background:var(--white);border:1px solid #ccc;
  font-family:Arimo,sans-serif;font-size:11px;color:#888;padding:7px 10px}
.subscribe{left:390px;top:933px;width:89px;height:25px;border:1px solid #aaa;border-radius:3px;
  background:linear-gradient(#fff 0%,#444 40%,#000);color:var(--white);font-family:Arimo,sans-serif;
  font-weight:700;font-size:11px;text-align:center;line-height:23px}
.footer-logo{right:200px;top:868px;font-size:36px;color:var(--white)}
.footer-rule{left:199px;top:976px;width:802px;height:1px;background:#777}
.legal{top:987px;font-size:9px;color:var(--white)}
.legal.menu{left:648px;word-spacing:6px}
</style>
</head>
<body>
<div class="abs topbar">
  <div class="links">Sell &nbsp;|&nbsp; Registry &nbsp;|&nbsp; Community &nbsp;|&nbsp; Blogs &nbsp;|&nbsp; Mobile &nbsp;|&nbsp; Gift Cards</div>
  <div class="account">Help &nbsp;|&nbsp; Email &nbsp;|&nbsp; Register</div>
</div>

<div class="abs logo header-logo">GlossNest</div>

<div class="abs cart">
  <svg width="24" height="20" viewBox="0 0 24 20"><path d="M1 2h4l3 11h12l3-8H7" fill="none" stroke="#222" stroke-width="2"/><circle cx="10" cy="17" r="2" fill="#222"/><circle cx="19" cy="17" r="2" fill="#222"/></svg>
  Shopping Cart
</div>
<div class="abs social"><span></span><span></span><span></span><span></span></div>

<div class="abs search">Search Items &amp; Shops<span class="sep"></span>
  <svg width="14" height="14" viewBox="0 0 14 14"><circle cx="5.5" cy="5.5" r="4" fill="none" stroke="#555" stroke-width="1.8"/><path d="M8.5 8.5l4 4" stroke="#555" stroke-width="2"/></svg>
</div>

<nav class="abs nav">
  <a>PRODUCT</a><a>DESCRIPTION</a><a>BUY NOW</a><a>CART</a><a>OUR POLICY</a><a>CONTACT US</a>
</nav>

<section class="abs banner">
  <div class="abs photo-organizer" role="img" aria-label="Clear acrylic organizer filled with makeup"></div>
  <div class="abs photo-cosmetics" role="img" aria-label="Assorted cosmetics: lipstick, mascara, eyeshadow, powder and foundation"></div>
  <h1>ACRYLIC MAKEUP ORGANIZER</h1>
  <p>FOR EASE OF USE.</p>
  <svg style="left:5px" width="18" height="34" viewBox="0 0 18 34"><path d="M16 1L2 17l14 16" fill="none" stroke="#ddd" stroke-width="1.5"/></svg>
  <svg style="right:5px" width="18" height="34" viewBox="0 0 18 34"><path d="M2 1l14 16L2 33" fill="none" stroke="#ddd" stroke-width="1.5"/></svg>
</section>

<div class="abs product-photo" role="img" aria-label="Six-drawer clear acrylic organizer with lid on dark cloth"></div>

<p class="abs intro">As a women we have way too many hair and makeup products. Some we keep because we bought it and are stuck with them, some we can't part with. It's a lot of work and money to keep up with all the new "IT" items. They are scattered in medicine cabinets, make shift storage bins, any where we can find space. In the end its just a mess. Trying to find it, wondering where you put it, or did I run out.</p>
<div class="abs rule" style="top:644px"></div>

<ul class="abs features">
  <li class="sm">6 Draws with an Open Top lid</li>
  <li class="sm">15" Wide x 12" L x 12" D</li>
  <li>Top draw is approximately 3" tall</li>
  <li>Each additional draw is approximately 2" tall.</li>
  <li>Every organizer is wrapped to protect from scratches during shipping.</li>
  <li>It is then surrounded by four sides of thick solid styrofoam.</li>
  <li>Then placed into a heavy durable box for shipping</li>
</ul>
<div class="abs rule" style="top:786px"></div>

<div class="abs buy">BUY NOW</div>
<div class="abs price">$159</div>
<a class="abs learn">Learn More</a>

<footer class="abs footer"></footer>
<div class="abs news-title">Subcribe To Newsletter</div>
<div class="abs email">Enter Your Email Address</div>
<div class="abs subscribe">Subcribe</div>
<div class="abs logo footer-logo">GlossNest</div>
<div class="abs footer-rule"></div>
<div class="abs legal" style="left:201px">© 2013 GlossNest.example</div>
<div class="abs legal" style="left:406px">English (US) / $ United States Dollar / Everywhere</div>
<div class="abs legal menu">Blog About Contact Press Developers Careers Terms Privacy Copyright</div>
</body>
</html>
```